Wordpress template re-design of current website

We need a WordPress template design and new look for our existing website. Our existing site it located at www.velquor.com.au We are a tech company and want a fresh, clean modern website that matches our brand, services and logo colors. Our main Services are hospitality solutions, Velquor TV solution and managed networks, more information on these can come from our existing website.

Target Market(s)

We are a tech company so must have a modern feel for new technology

Industry/Entity Type

It Company

Number of Pages Required

5+ page

Font styles to use
Sans Serif

Requirements
Must have
• Be based on a wordpress templete design and match the services that we have in our existing website, in the testimonials want a place for video testimonials as well as text. Nice clean icons used for graphics to represent services.
Nice to have
• nice visual representation of our services in the way of clean icons etc
Should not have
• Clutter

```html
<!DOCTYPE html>
<html lang="en">
<head>
<meta charset="utf-8">
<title>Velquor – Mobile Gateways</title>
<link href="https://fonts.googleapis.com/css2?family=Lato:ital,wght@0,300;0,400;0,700;0,900;1,300;1,400;1,700;1,900&display=swap" rel="stylesheet">
<style>
:root{
  --brand:#0d4f9e;
  --band:#0a4fa0;
  --band-dark:#0846919e;
  --ink:#2a2a2a;
  --muted:#b9b9b9;
  --strip:#f3f3f3;
  --white:#ffffff;
}
*{margin:0;padding:0;box-sizing:border-box}
html,body{width:1200px;height:1200px;overflow:hidden;background:var(--white);font-family:'Lato',sans-serif;color:var(--ink)}
.page{position:relative;width:1200px;height:1200px}
.partners{position:absolute;top:0;left:0;width:1200px;height:48px;background:var(--strip);display:flex;justify-content:space-between;align-items:center;padding:0 160px 8px}
.partners span{font-size:13px;font-weight:700;color:#555;letter-spacing:.5px}
.gateways{position:absolute;top:48px;left:0;width:1200px;height:342px}
.device-art{position:absolute;left:160px;top:86px;width:86px;height:172px;border-radius:14px;background:linear-gradient(160deg,#3a3a3a,#0f0f0f)}
.device-art::after{content:"";position:absolute;left:7px;top:28px;right:7px;bottom:30px;background:linear-gradient(180deg,#e8e8e8,#b88a56 55%,#dcdcdc);border-radius:2px}
.gateways h1{position:absolute;top:88px;width:1200px;text-align:center;font-size:34px;font-weight:700;color:var(--brand);letter-spacing:-.3px}
.gateways .tag{position:absolute;top:131px;width:1200px;text-align:center;font-size:12px;color:#444}
.rule{position:absolute;height:4px;background:#c8c8c8;left:50%;transform:translateX(-50%)}
.gateways .rule{top:154px;width:122px}
.gateways p{position:absolute;top:178px;left:268px;width:664px;text-align:center;font-size:12.4px;line-height:20px;color:#333}
.advantage{position:absolute;top:390px;left:0;width:1200px;height:618px;background:var(--band)}
.advantage h2{position:absolute;top:64px;width:1200px;text-align:center;font-size:32px;font-weight:700;color:var(--white)}
.advantage .lead{position:absolute;top:109px;width:1200px;text-align:center;font-size:15px;line-height:18px;font-style:italic;font-weight:300;color:var(--white)}
.advantage .rule{top:161px;width:362px;background:#b8c4d6;height:3px}
.feature{position:absolute;left:0;width:640px;height:78px;background:linear-gradient(90deg,#0847939c 0%,#08479399 70%,rgba(8,71,147,0) 100%);display:flex;align-items:center;padding-left:160px}
.feature svg{width:42px;height:52px;margin-right:10px;flex:none}
.feature h3{font-size:18px;font-weight:900;font-style:italic;color:var(--white);letter-spacing:-.2px}
.feature p{font-size:11.6px;font-style:italic;color:var(--white);margin-top:2px}
.devices-art{position:absolute;left:680px;top:235px;width:360px;height:300px;border-radius:18px;background:linear-gradient(135deg,#1b1b1b,#2d5fa8 50%,#1a1a1a)}
.hello{position:absolute;top:1008px;left:0;width:1200px;height:192px}
.hello h2{position:absolute;left:160px;top:54px;font-size:50px;font-weight:900;color:var(--brand);letter-spacing:-1px}
.hello .underline{position:absolute;left:160px;top:110px;width:172px;height:4px;background:#c8c8c8}
.contact{position:absolute;left:160px;display:flex;align-items:center;font-size:12.5px;font-weight:700;color:#222}
.contact svg{margin-right:6px}
.map-frame{position:absolute;left:582px;top:117px;width:458px;height:90px;background:var(--white);box-shadow:0 0 6px rgba(0,0,0,.18);padding:14px 13px 0}
.map-frame div{width:100%;height:100%;background:linear-gradient(120deg,#e9e5dc,#dcd7cc 60%,#e4eadf)}
</style>
</head>
<body>
<div class="page">
  <div class="partners">
    <span>HARBOURLINE</span><span>KESTREL</span><span>SOLACE</span><span>ROAMWELL</span><span>BRIGHTMERE</span><span>WANDERLY</span><span>IRONVALE</span><span>TIDEWATER</span>
  </div>

  <section class="gateways">
    <div class="device-art" role="img" aria-label="Smartphone showing a client website"></div>
    <h1>Anytime Anywhere Mobile Gateways</h1>
    <div class="tag">CREATING SOLUTIONS THAT WORK.</div>
    <div class="rule"></div>
    <p>Instant internet connectivity has become a basic need. No matter where someone travels, they expect it. Velquor applies its IT expertise to deliver a stable, reliable wireless solution in environments where the traditional broadband connection is not viable. Think passenger trains, boats, outdoor events, or a remote location. Our mobile <b>3G</b> and <b>4G</b> access points provides clients with connectivity solutions <b>anytime, anywhere</b></p>
  </section>

  <section class="advantage">
    <h2>The Velquor Advantage</h2>
    <div class="lead">Velquor mobile solutions allow your guests to keep in touch whilst travelling,<br>allowing them to post to social media what a great day they are having with your company.</div>
    <div class="rule"></div>

    <div class="feature" style="top:217px">
      <svg viewBox="0 0 42 52" fill="none" stroke="#fff" stroke-width="2.5"><path d="M10 6a9 9 0 0 1 12 0M13 10a5 5 0 0 1 6 0"/><rect x="8" y="18" width="16" height="28" rx="3" transform="rotate(30 16 32)" fill="#fff"/></svg>
      <div><h3>3G and 4G options available</h3><p>With 3G and 4G options available mobile internet has never been easier</p></div>
    </div>
    <div class="feature" style="top:299px">
      <svg viewBox="0 0 42 52" fill="none" stroke="#fff" stroke-width="2.5"><path d="M6 8a10 10 0 0 1 14 0M9 12a5 5 0 0 1 8 0"/><rect x="4" y="18" width="18" height="30" rx="2" fill="#fff"/><path d="M22 30l8 4 6 14" /></svg>
      <div><h3>Remote Monitoring</h3><p>Clients can monitor their fleet from their office.</p></div>
    </div>
    <div class="feature" style="top:381px">
      <svg viewBox="0 0 42 52"><path d="M20 10l14 5v10c0 9-6 15-14 18-8-3-14-9-14-18V15z" fill="#fff"/><path d="M14 27l5 5 8-9" stroke="#0a4fa0" stroke-width="3" fill="none"/></svg>
      <div><h3>Security</h3><p>Fast, secure mobile options</p></div>
    </div>
    <div class="feature" style="top:464px">
      <svg viewBox="0 0 42 52" fill="#fff"><circle cx="20" cy="16" r="8"/><path d="M4 44c0-10 7-16 16-16s16 6 16 16z"/><circle cx="34" cy="42" r="6" fill="#0a4fa0" stroke="#fff" stroke-width="2"/></svg>
      <div><h3>On The Spot Support</h3><p>Our technical team provides 24/7 assistance.</p></div>
    </div>

    <div class="devices-art" role="img" aria-label="Three smartphones showing hospitality and gallery mobile sites"></div>
  </section>

  <section class="hello">
    <h2>HELLO!</h2>
    <div class="underline"></div>
    <div class="contact" style="top:146px">
      <svg width="24" height="14" viewBox="0 0 24 14"><path d="M0 3h5M2 7h3M0 11h5" stroke="#0d4f9e" stroke-width="1.5"/><rect x="7" y="1" width="17" height="12" fill="#0d4f9e"/><path d="M7 1l8.5 7L24 1" stroke="#fff" stroke-width="1.3" fill="none"/></svg>
      sales@velquor.com.au
    </div>
    <div class="contact" style="top:174px">
      <svg width="14" height="20" viewBox="0 0 14 20"><rect x="2" y="1" width="10" height="18" rx="2" fill="none" stroke="#0d4f9e" stroke-width="2"/></svg>
      &nbsp;1300 555 014
    </div>
    <div class="map-frame"><div role="img" aria-label="Street map showing the office location"></div></div>
  </section>
</div>
</body>
</html>
```